Zielgruppe
Wir sind ein Konzeptkaufhaus in Fulda. Im ehemaligen Lumora Gebäude in Fulda ist ein Pop-Up Shop Konzept Namens Fritz Konzeptkaufhaus entstanden. Hier können lokale und Nischenhändler von kleinen Tischflächen bis größeren Freiflächen verschiedene Optionen anmieten, um Ihre Artikel anzubieten. Es wird über eine zentrale Kasse abgewickelt und erfordert keinen weiteren Personalaufwand. Zielgruppe sind lokale Kunden, die regionale Anbieter unterstützen möchten sowie Touristen. Aber generell auch jeder Offline Shopper, der besondere Artikel sucht, die nicht an jeder Ecke zu erwerben sind
Aufgabenstellung
Es soll ein Layout für ein Bauzaun Plakat entstehen. Hier gibt es einen Entwurf, der aber zu Textlastig ist. Fest steht die Schrifttypen und Faben im Anhang. Auf Canva verwendete Schrifttypen Gliker & Gagalin. Ich hätte gerne anstatt der vielen Texte kurze Statements und dafür einige Fotos - von außen/innen, damit der Betrachter mehr damit anfangen kann

```html
<!DOCTYPE html>
<html lang="de">
<head>
<meta charset="utf-8">
<title>Fritz Konzeptkaufhaus – Bauzaun-Plakat</title>
<link href="https://fonts.googleapis.com/css2?family=Rubik+Dirt&display=swap" rel="stylesheet">
<style>
  :root {
    --page: #ffffff;
    --sky: #86d0de;
    --sky-deep: #6fb6cc;
    --brand-pink: #e31c4b;
    --ink: #231f20;
    --strip: #ffffff;
  }
  html, body {
    margin: 0;
    padding: 0;
    width: 1200px;
    height: 1200px;
    overflow: hidden;
    background: var(--page);
  }
  .poster {
    position: absolute;
    left: 40px;
    top: 301px;
    width: 1120px;
    height: 597px;
    font-family: "Rubik Dirt", "Arial Black", sans-serif;
    color: var(--ink);
  }
  .hero {
    position: absolute;
    inset: 0 0 120px 0;
    background: linear-gradient(180deg, var(--sky) 0%, var(--sky-deep) 55%, var(--sky) 100%);
    overflow: hidden;
  }
  .hero-backdrop {
    position: absolute;
    inset: 0;
    background: linear-gradient(90deg, rgba(111,182,204,0.0) 0%, rgba(95,165,190,0.45) 40%, rgba(111,182,204,0.15) 100%);
  }
  .brand-name {
    position: absolute;
    left: 60px;
    top: 50px;
    width: 700px;
    margin: 0;
    font-size: 58px;
    font-weight: 400;
    line-height: 64px;
    color: var(--brand-pink);
    letter-spacing: 1px;
  }
  .brand-name span {
    display: block;
    white-space: nowrap;
  }
  .statements {
    position: absolute;
    left: 60px;
    top: 225px;
    margin: 0;
    padding: 0;
    list-style: none;
  }
  .statements li {
    font-size: 53px;
    line-height: 76px;
    letter-spacing: 5px;
    white-space: nowrap;
    text-transform: uppercase;
  }
  .shop-photo {
    position: absolute;
    left: 798px;
    top: 46px;
    width: 261px;
    height: 389px;
    border-radius: 14px;
    background: linear-gradient(160deg, #8a6a58 0%, #3b3030 40%, #d9d4cf 85%, #efece8 100%);
    box-shadow: 8px 8px 0 var(--ink);
  }
  .contact-strip {
    position: absolute;
    left: 0;
    right: 0;
    bottom: 0;
    height: 120px;
    background: var(--strip);
    border-top: 1px solid var(--ink);
    box-sizing: border-box;
  }
  .address, .reach {
    position: absolute;
    top: 22px;
    margin: 0;
    font-style: normal;
    font-size: 32px;
    line-height: 46px;
    letter-spacing: 3px;
    text-transform: uppercase;
    white-space: nowrap;
  }
  .address { left: 60px; }
  .reach { right: 62px; text-align: right; }
</style>
</head>
<body>
  <section class="poster">
    <div class="hero">
      <div class="hero-backdrop" role="img" aria-label="Getöntes Foto des Kaufhausteams vor der Ladenfassade"></div>
      <h1 class="brand-name"><span>Fritz Konzept</span><span>kaufhaus</span></h1>
      <ul class="statements">
        <li>Regionale Werte.</li>
        <li>Globales Handwerk.</li>
        <li>Innovative Marken.</li>
      </ul>
      <div class="shop-photo" role="img" aria-label="Foto: Händlerin arrangiert Drucke und Bilderrahmen an ihrem Verkaufstisch"></div>
    </div>
    <footer class="contact-strip">
      <address class="address">Lindenallee 7,<br>36041 Fulda</address>
      <p class="reach">+49 661 / 555 0182<br>hallo@fritz-kaufhaus.de</p>
    </footer>
  </section>
</body>
</html>
```